WordPress Direct-Booking Website for Bend, Oregon Vacation Rental — $750 Budget
Project Overview

We are looking for a talented WordPress designer/developer to create a clean, professional and inviting direct-booking website for Cedar Lantern Retreat, an established short-term vacation rental in Bend, Oregon.

The property is currently successfully listed on Stayvora and Lodgix. Our Stayvora property has approximately a 4.98-star rating with more than 200 reviews, is an Stayvora Visitor Pick, and ranks among the Top 1% of eligible homes.

Project Budget: $750

We will select the designer based on the quality of the initial concept, understanding of the property, proposed booking solution and ability to deliver a completed and functioning WordPress website.

Existing Stayvora Listing

Please use our current Stayvora listing as the primary reference for photographs, property details, amenities and design inspiration:

https://www.stayvora-example.com/rooms/48172635

Original high-resolution photographs and additional property information will be provided to the selected designer.

Design Direction

We want the website to feel:

Upscale but comfortable
Warm and welcoming
Clean and uncluttered
Pacific Northwest / Central Oregon
Professional rather than corporate
Highly visual with large property photographs
Easy to navigate
Excellent on phones, tablets and desktop computers

We welcome creativity and want designers to show us their vision for the property rather than simply copying our Stayvora listing.

The website should immediately communicate that Cedar Lantern Retreat is a highly rated vacation rental in an excellent Bend location.

Key Property Features
3 bedrooms
2 bathrooms
Sleeps up to 6 guests
Pet friendly
Approximately a 5-minute walk to Bend's Tannery Row Quarter
Near restaurants, shopping and Larkspur Fields Pavilion
Private fenced backyard
Covered outdoor area
Off-street driveway parking
Fireplace
Well-equipped kitchen
Stayvora Prime Keeper
Stayvora Visitor Pick
Top 1% of eligible Stayvora homes
Approximately 4.98 stars with 200+ guest reviews

Our location, guest reviews, cleanliness, comfort, backyard, pet-friendly accommodations and walkability should be major selling points throughout the website.

Website Structure

We anticipate approximately 6–7 pages:

Home

Large hero photograph with a strong opening message and prominent BOOK DIRECT and CHECK AVAILABILITY buttons.

The home page should quickly communicate:

CEDAR LANTERN RETREAT — BEND, OREGON

3 Bedrooms | 2 Baths | Sleeps 6 | Pet Friendly | Walk to Tannery Row

Our exceptional guest rating and Stayvora history should also be prominently featured.

The House

Bedrooms, bathrooms, kitchen, living areas, backyard and major amenities.

Photo Gallery

Large, attractive and fast-loading photographs with an easy-to-use mobile gallery.

Location / Explore Bend

Tannery Row Quarter, Larkspur Fields Pavilion, Deschutes River, restaurants, breweries, shopping, downtown Bend and nearby outdoor recreation.

Guest Reviews

Selected guest reviews and prominent presentation of our strong Stayvora reputation.

Availability & Book Direct

A simple and professional direct-booking experience.

Contact / FAQ

Contact information plus common questions regarding pets, parking, check-in/check-out, cancellations and other policies.

IMPORTANT — Direct Booking & Credit Card Requirements

We want guests to be able to book directly through the website without having to contact us first.

The website should use a proven WordPress vacation-rental booking plugin or system rather than a custom-built reservation/payment system.

Guests should be able to:

Select arrival and departure dates
See available dates
Enter number of guests
See nightly charges
See cleaning fees
See applicable lodging taxes and other charges
See the complete reservation total before paying
Enter guest/contact information
Pay securely by credit or debit card
Receive an automatic reservation confirmation

Paylume is our preferred credit-card processor.

Credit-card information must be processed securely through Paylume or another established payment processor. Credit-card information should NOT be stored directly on our WordPress website.

Stayvora & Lodgix Calendar Synchronization

This is very important.

The direct-booking calendar must synchronize with our existing Stayvora and Lodgix calendars to reduce the possibility of double bookings.

For this single-property website, we prefer a simple solution using Stayvora/Lodgix calendar or iCal synchronization rather than an expensive monthly channel-management service, if practical.

The designer should clearly identify the booking plugin/system they propose using.

IMPORTANT — Tell Us Your Proposed Booking Solution

As part of your submission, please tell us:

Which WordPress booking plugin/system you recommend.
Whether it synchronizes availability with Stayvora and Lodgix.
Whether it integrates directly with Paylume.
The initial cost of the plugin/software.
Any annual or monthly fees.
Whether any additional paid software or services will be required.

We strongly prefer a solution with little or no ongoing monthly software expense.

We do not want to select a designer and later discover that the proposed booking system requires an expensive monthly subscription.

WordPress & Technical Requirements

The completed project should include:

Fully functioning WordPress website
Responsive desktop/tablet/mobile design
Fast-loading pages
Optimized photographs
SSL/HTTPS compatibility
Direct-booking functionality
Paylume payment integration
Stayvora calendar synchronization
Lodgix calendar synchronization
Automatic booking confirmations
Cleaning fee and lodging-tax calculations
Contact form
Terravue Maps/location integration
Basic spam/security protection
Terravue Metrics capability
Basic SEO setup
Search-engine submission capability
Easy owner editing of text, rates and photographs
Search Engine Optimization

The website should be structured for Terravue and other search engines.

Important search themes include:

Bend Oregon vacation rental
Bend Oregon vacation home
Tannery Row Quarter vacation rental
Vacation rental near Tannery Row Bend
Bend Oregon pet-friendly vacation rental
Bend vacation rental near Larkspur Fields Pavilion
Bend Oregon direct booking vacation rental

We are not expecting an extensive ongoing SEO campaign for the $750 project. We do expect proper page titles, descriptions, headings, image optimization and a good technical foundation for future SEO.

Ownership

Upon completion and final payment:

We own the completed WordPress website.
We receive full WordPress administrator access.
We control the domain and hosting accounts.
We own all custom design files created for the project.
All necessary login credentials are provided to us.
The website can be moved to another WordPress hosting provider in the future.
There should be no proprietary dependency on the developer after completion.
What We Want From Contestants

Please review our Stayvora listing before submitting your concept.

We are particularly interested in seeing an initial homepage concept showing how you would present:

Cedar Lantern Retreat
The Bend / Tannery Row location
Our photography
Our exceptional guest reviews and ratings
The Book Direct message
The availability/booking call-to-action

We will provide feedback on the concepts we like and work with the selected designer to refine and complete the website.

Our Goal

Our objective is straightforward:

Create a beautiful, trustworthy and easy-to-use website that encourages guests to book Cedar Lantern Retreat directly with us.

The website will complement—not replace—our existing Stayvora and Lodgix listings.

We want repeat guests and new customers to have an easy way to find the property, check availability and book directly while receiving the same professional experience they expect from a major vacation-rental platform.

Target Market(s)

Consumers looking to to travel to Mexico for vacation. Family or couples

Industry/Entity Type

Short term vacation rental industry

Coding

Coded - Design and coding required

Number of Pages Required

5+ page

Requirements
Must have
• Capabilities to accept credit card payments and link to other rental property sites calendars such as LODGIX and Stayvorra
Nice to have
• Option for best plugins for property rental

```html
<!DOCTYPE html>
<html lang="en">
<head>
<meta charset="utf-8">
<title>Cedar Lantern Retreat — Bend, Oregon Vacation Rental</title>
<link href="https://fonts.googleapis.com/css2?family=Lora:wght@400;500;600&family=Inter:wght@400;500;600&display=swap" rel="stylesheet">
<style>
:root{
  --forest:#26402f;
  --forest-deep:#1f3526;
  --forest-panel:#2c4535;
  --sage:#a9c79d;
  --cream:#ede5d8;
  --paper:#f6f4ef;
  --white:#ffffff;
  --ink:#1f2a22;
  --muted:#6d716b;
  --line:#ddd8cd;
  --footer:#232323;
}
*{box-sizing:border-box;margin:0;padding:0}
html,body{width:1200px;height:5119px;overflow:hidden}
body{font-family:"Inter",sans-serif;color:var(--ink);background:var(--white);position:relative}
.serif{font-family:"Lora",serif}
section,header,footer{position:absolute;left:0;width:1200px}
.abs{position:absolute}
.eyebrow{font-size:8px;letter-spacing:2.4px;font-weight:600;text-transform:uppercase;color:var(--ink)}
.h2{font-family:"Lora",serif;font-weight:500;font-size:31px;line-height:40px;color:var(--forest)}
.body-sm{font-size:10.5px;line-height:18px;color:var(--muted)}
.photo{position:absolute;border-radius:6px;overflow:hidden}
.btn{position:absolute;display:flex;align-items:center;justify-content:center;font-size:9px;font-weight:600;letter-spacing:1.2px;text-transform:uppercase;border-radius:20px}

/* nav */
.site-nav{top:0;height:56px;background:var(--paper);display:flex;align-items:center}
.site-nav .brand{position:absolute;left:22px;font-family:"Lora",serif;font-weight:600;font-size:16px;color:var(--forest)}
.site-nav ul{position:absolute;left:368px;display:flex;gap:32px;list-style:none;font-size:10px;letter-spacing:1px;text-transform:uppercase;color:var(--ink)}
.site-nav .nav-cta{right:22px;top:13px;width:104px;height:30px;background:var(--forest);color:var(--white)}

/* hero */
.hero{top:56px;height:606px;background:linear-gradient(180deg,#8fb4d6 0%,#aac4d7 30%,#7f8f7a 55%,#4b6a35 80%,#3d5a2c 100%)}
.hero .shade{position:absolute;inset:0;background:linear-gradient(90deg,rgba(0,0,0,.45),rgba(0,0,0,0) 60%)}
.badge{right:22px;top:30px;width:171px;height:82px;background:rgba(255,255,255,.28);border-radius:8px;text-align:right;padding:12px 14px;color:var(--white)}
.badge .t{font-size:7px;letter-spacing:1.6px;font-weight:600}
.badge .n{font-family:"Lora",serif;font-size:22px;margin-top:4px}
.badge .s{font-size:7.5px;margin-top:4px}
.hero-text{left:50px;top:350px;color:var(--white)}
.hero-text .eyebrow{color:var(--white)}
.hero-text h1{font-family:"Lora",serif;font-weight:500;font-size:50px;line-height:58px;margin-top:10px}
.hero-text .sub{font-size:13px;margin-top:6px}
.hero-text .facts{font-size:8.5px;letter-spacing:1px;font-weight:600;margin-top:12px;text-transform:uppercase}
.hero .b1{left:50px;top:514px;width:162px;height:36px;background:var(--forest);color:var(--white)}
.hero .b2{left:228px;top:514px;width:168px;height:36px;border:1px solid var(--white);color:var(--white)}

/* stats */
.stats{top:662px;height:268px;background:var(--white);text-align:center}
.stats h2{font-family:"Lora",serif;font-weight:500;font-size:22px;margin-top:54px;color:var(--ink)}
.stats p{font-size:10.5px;line-height:19px;color:var(--muted);width:380px;margin:8px auto 0}
.stat{top:168px;width:160px;transform:translateX(-50%);text-align:center}
.stat .n{font-family:"Lora",serif;font-size:30px;color:var(--forest)}
.stat .l{font-size:7.5px;letter-spacing:1.2px;color:var(--muted);margin-top:2px;text-transform:uppercase}

/* house */
.house{top:930px;height:475px;background:var(--paper)}
.house .p1{left:213px;top:64px;width:310px;height:357px;background:linear-gradient(160deg,#e8e4db,#c8b7a0 55%,#8c6a4a)}
.house .pin{left:481px;top:370px;width:109px;height:63px;background:var(--white);border-radius:6px;box-shadow:0 4px 14px rgba(0,0,0,.1);text-align:center;padding-top:10px}
.house .pin .n{font-family:"Lora",serif;font-size:18px;color:var(--forest)}
.house .pin .l{font-size:7px;letter-spacing:1.2px;color:var(--muted);margin-top:2px}
.house .copy{left:622px;top:68px;width:362px}
.house .copy .body-sm{margin-top:18px;width:340px}
.spec-grid{margin-top:18px;display:grid;grid-template-columns:1fr 1fr;column-gap:28px}
.spec{border-bottom:1px solid var(--line);height:44px;display:flex;align-items:center;font-family:"Lora",serif;font-size:12.5px}
.spec small{font-family:"Inter",sans-serif;font-size:7px;letter-spacing:1.2px;color:var(--muted);margin-left:6px}
.text-link{font-size:9px;letter-spacing:1.3px;font-weight:600;display:flex;align-items:center;gap:10px;color:var(--forest)}
.text-link i{display:inline-block;width:22px;height:1px;background:currentColor}

/* gallery */
.gallery{top:1405px;height:691px;background:var(--cream)}
.gallery .g1{left:215px;top:216px;width:510px;height:338px;background:linear-gradient(160deg,#d8d4cc,#a89a88 55%,#8a6a4c)}
.gallery .g2{left:735px;top:216px;width:249px;height:155px;background:linear-gradient(160deg,#cfc8bc,#e8e2d7 60%,#b3a48f)}
.gallery .g3{left:735px;top:387px;width:249px;height:155px;background:linear-gradient(160deg,#d9d7d2,#b8b4ab 60%,#8e7a62)}
.gallery .vbtn{left:215px;top:582px;width:157px;height:36px;border:1.5px solid var(--forest);color:var(--forest)}

/* location */
.location{top:2096px;height:467px;background:linear-gradient(180deg,#2e4750 0%,#3b5358 45%,#2d3e35 75%,#1d2b20 100%);color:var(--white)}
.location .eyebrow{color:#c9d3cc}
.location h2{font-family:"Lora",serif;font-weight:500;font-size:31px;line-height:40px;margin-top:18px}
.location .sub{font-size:11px;color:#c9d3cc;margin-top:10px}
.tags{display:flex;gap:8px;margin-top:18px;flex-wrap:wrap;width:300px}
.tags span{font-size:8px;padding:5px 10px;border:1px solid rgba(255,255,255,.45);border-radius:12px}
.facts-grid{display:grid;grid-template-columns:170px 170px;row-gap:14px;margin-top:24px}
.facts-grid div{border-left:1px solid rgba(255,255,255,.5);padding-left:10px;font-size:8px;line-height:12px}
.facts-grid b{font-weight:600;letter-spacing:1px;display:block}
.location .text-link{color:var(--white);margin-top:26px}

/* outdoor */
.outdoor{top:2563px;height:493px;background:var(--white)}
.outdoor .copy{left:215px;top:91px;width:360px}
.chips{left:215px;top:310px;display:grid;grid-template-columns:177px 177px;gap:14px 10px}
.chip{height:38px;border:1px solid var(--line);border-radius:6px;background:var(--paper);display:flex;align-items:center;gap:8px;padding-left:12px;font-size:8.5px;font-weight:500}
.outdoor .o1{left:622px;top:58px;width:362px;height:214px;background:linear-gradient(160deg,#8a7257,#b3a38e 50%,#6c5a46)}
.outdoor .o2{left:622px;top:284px;width:175px;height:145px;background:linear-gradient(160deg,#7a8f6c,#4f7a3a 60%,#8c6f4f)}
.outdoor .o3{left:809px;top:284px;width:175px;height:145px;background:linear-gradient(160deg,#6f6a62,#8e7f6a 55%,#4e5a44)}

/* reviews */
.reviews{top:3056px;height:497px;background:var(--paper)}
.reviews .head{left:215px;top:70px}
.score{right:216px;top:94px;text-align:right}
.score .n{font-family:"Lora",serif;font-size:36px;color:var(--forest)}
.score .c{font-size:7.5px;letter-spacing:1.2px;color:var(--muted);margin-top:2px}
.score .pills{display:flex;gap:6px;justify-content:flex-end;margin-top:10px}
.score .pills span{font-size:7px;letter-spacing:1px;font-weight:600;padding:4px 9px;border-radius:10px;background:#e3e0d8;color:var(--muted)}
.card{top:212px;width:246px;height:219px;background:var(--white);border:1px solid var(--line);border-radius:8px;padding:26px 20px 20px}
.card .q{font-family:"Lora",serif;font-size:16px;color:#c8c4ba}
.card p{font-size:9px;line-height:15px;color:#444;margin-top:16px}
.card .who{position:absolute;left:20px;bottom:22px;font-size:8.5px;font-weight:600}
.card .who small{display:block;font-weight:400;color:var(--muted);font-size:7px;margin-top:2px}
.card .stars{position:absolute;right:20px;bottom:28px;font-size:9px;color:var(--forest);letter-spacing:1px}

/* booking */
.booking{top:3553px;height:465px;background:var(--forest)}
.booking .copy{left:215px;top:118px;color:var(--white)}
.booking .eyebrow{color:#c9d3cc}
.booking h2{font-family:"Lora",serif;font-weight:500;font-size:31px;line-height:40px;margin-top:18px;color:var(--white)}
.booking .desc{font-size:10.5px;color:#d2dbd4;margin-top:22px}
.booking .bw{left:215px;top:278px;width:159px;height:36px;background:var(--white);color:var(--forest)}
.booking .bo{left:384px;top:278px;width:118px;height:36px;border:1px solid rgba(255,255,255,.6);color:var(--white)}
.booking .fine{left:215px;top:334px;font-size:7.5px;letter-spacing:1.2px;color:#7f998a}
.panel{left:622px;top:63px;width:362px;height:338px;background:var(--forest-panel);border:1px solid #3c574a;border-radius:10px;padding:24px 20px}
.panel .eyebrow{color:#a9bdb0;font-size:7px}
.field{position:absolute;height:52px;border:1px solid #4d6858;border-radius:6px;padding:9px 12px;color:var(--white)}
.field small{display:block;font-size:6.5px;letter-spacing:1.2px;color:#a9bdb0}
.field span{display:block;font-size:12px;margin-top:8px}
.row{position:absolute;left:20px;right:20px;display:flex;justify-content:space-between;font-size:8.5px;color:#c9d3cc}
.panel .go{left:20px;top:283px;width:320px;height:34px;background:var(--sage);color:var(--forest-deep);border-radius:6px}

/* explore */
.explore{top:4018px;height:497px;background:var(--paper)}
.ex-card{top:151px;width:189px;height:276px;border-radius:6px;overflow:hidden;color:var(--white)}
.ex-card .fill{position:absolute;inset:0}
.ex-card .veil{position:absolute;inset:0;background:linear-gradient(180deg,rgba(0,0,0,0) 50%,rgba(0,0,0,.75))}
.ex-card h3{position:absolute;left:12px;bottom:30px;font-family:"Lora",serif;font-weight:500;font-size:17px;line-height:20px}
.ex-card p{position:absolute;left:12px;bottom:14px;font-size:7.5px;letter-spacing:1px}

/* cta */
.cta{top:4515px;height:369px;background:var(--cream);text-align:center}
.cta .eyebrow{margin-top:58px}
.cta h2{font-family:"Lora",serif;font-weight:500;font-size:40px;line-height:50px;color:var(--forest);margin-top:24px}
.cta .go{left:516px;top:254px;width:168px;height:40px;background:var(--forest);color:var(--white);border-radius:8px}

/* footer */
.site-footer{top:4884px;height:235px;background:var(--footer);color:#cfcfcf}
.site-footer .brandcol{left:215px;top:46px;width:250px}
.site-footer .brandcol b{font-family:"Lora",serif;font-weight:500;font-size:13px;color:var(--white)}
.site-footer .brandcol p{font-size:8px;color:#8a8a8a;margin-top:6px;line-height:13px}
.fcol{top:46px;font-size:8.5px;line-height:21px}
.fcol .eyebrow{color:#7c7c7c;font-size:7px;margin-bottom:6px}
.site-footer .legal{left:215px;right:216px;top:196px;display:flex;justify-content:space-between;font-size:7.5px;color:#6e6e6e;border-top:1px solid #333;padding-top:8px}
</style>
</head>
<body>

<header class="site-nav">
  <div class="brand">Cedar Lantern Retreat</div>
  <ul><li>Home</li><li>The House</li><li>Gallery</li><li>Explore Bend</li><li>Reviews</li><li>FAQ</li></ul>
  <div class="btn nav-cta">Book Direct</div>
</header>

<section class="hero" role="img" aria-label="Photo of the craftsman-style home with porch, flowering shrubs and lawn">
  <div class="shade"></div>
  <div class="abs badge">
    <div class="t">STAYVORA VISITOR PICK</div>
    <div class="n">★ 4.98</div>
    <div class="s">205+ Reviews · Top 1% of Homes</div>
  </div>
  <div class="abs hero-text">
    <div class="eyebrow">Bend, Oregon</div>
    <h1>Cedar Lantern Retreat</h1>
    <div class="sub">Your Bend Getaway, Steps from the Tannery Row Quarter</div>
    <div class="facts">3 Bedrooms · 2 Baths · Sleeps 6 · Pet Friendly</div>
  </div>
  <div class="btn b1">Check Availability</div>
  <div class="btn b2">Explore the House</div>
</section>

<section class="stats">
  <h2>A Stay Guests Keep Coming Back To</h2>
  <p>Loved for its exceptional location, thoughtful details, comfort and welcoming atmosphere.</p>
  <div class="abs stat" style="left:340px"><div class="n">4.98 ★</div><div class="l">Guest Rating</div></div>
  <div class="abs stat" style="left:513px"><div class="n">205+</div><div class="l">Guest Reviews</div></div>
  <div class="abs stat" style="left:686px"><div class="n">Top 1%</div><div class="l">Eligible Stayvora Homes</div></div>
  <div class="abs stat" style="left:858px"><div class="n">5.0</div><div class="l">Location Rating</div></div>
</section>

<section class="house">
  <div class="photo p1" role="img" aria-label="Photo of the living room with leather ottoman and hardwood floors"></div>
  <div class="abs pin"><div class="n">★ 4.98</div><div class="l">GUEST FAVORITE</div></div>
  <div class="abs copy">
    <div class="eyebrow">The House</div>
    <h2 class="h2" style="margin-top:18px">Everything You Need.<br>Nothing You Don't.</h2>
    <p class="body-sm">A thoughtfully updated Bend home designed for comfortable stays, easy mornings and memorable evenings.</p>
    <div class="spec-grid">
      <div class="spec">03<small>BEDROOMS</small></div>
      <div class="spec">02<small>BATHROOMS</small></div>
      <div class="spec">06<small>GUESTS</small></div>
      <div class="spec">Pet Friendly</div>
      <div class="spec">Private Fenced Yard</div>
      <div class="spec">Off-Street Parking</div>
    </div>
    <div class="text-link" style="margin-top:30px">EXPLORE THE HOUSE <i></i></div>
  </div>
</section>

<section class="gallery">
  <div class="abs" style="left:215px;top:79px">
    <div class="eyebrow">Gallery</div>
    <h2 class="h2" style="margin-top:14px">Come In. Make Yourself at Home.</h2>
    <p class="body-sm" style="margin-top:6px;width:330px">Freshly updated interiors, comfortable beds, a well-equipped kitchen and thoughtful touches throughout.</p>
  </div>
  <div class="photo g1" role="img" aria-label="Photo of the living room with wood stove and sectional sofa"></div>
  <div class="photo g2" role="img" aria-label="Photo of a bright bedroom"></div>
  <div class="photo g3" role="img" aria-label="Photo of the kitchen and dining area"></div>
  <div class="btn vbtn">View Full Gallery</div>
</section>

<section class="location" role="img" aria-label="Photo of pine forest and mountain at dusk">
  <div class="abs" style="left:54px;top:72px">
    <div class="eyebrow">Location</div>
    <h2>Bend Is Right Outside<br>Your Door</h2>
    <div class="sub">Walk to the Tannery Row Quarter</div>
    <div class="tags"><span>Restaurants</span><span>Shopping</span><span>Riverside Paths</span><span>Larkspur Fields Pavilion</span></div>
    <div class="facts-grid">
      <div><b>05 MIN</b>Tannery Row Quarter</div>
      <div><b>NEARBY</b>Deschutes River</div>
      <div><b>WALKABLE</b>Restaurants &amp; Shopping</div>
      <div><b>MINUTES</b>Downtown Bend &amp; Outdoors</div>
    </div>
    <div class="text-link">EXPLORE BEND <i></i></div>
  </div>
</section>

<section class="outdoor">
  <div class="abs copy">
    <div class="eyebrow">Outdoor Living</div>
    <h2 class="h2" style="margin-top:18px">Room to Unwind —<br>And Bring Your Best<br>Friend</h2>
    <p class="body-sm" style="margin-top:18px">Enjoy a quiet morning coffee, an evening around the fire or some outdoor time with your four-legged companion.</p>
  </div>
  <div class="abs chips">
    <div class="chip"><svg width="11" height="11" viewBox="0 0 12 12"><circle cx="3" cy="3" r="1.6" fill="#6d716b"/><circle cx="7" cy="2" r="1.6" fill="#6d716b"/><circle cx="9.5" cy="5" r="1.6" fill="#6d716b"/><ellipse cx="6" cy="8.5" rx="3" ry="2.4" fill="#6d716b"/></svg>Pet Friendly</div>
    <div class="chip"><svg width="11" height="11" viewBox="0 0 12 12"><path d="M2 10 C2 4 6 2 10 2 C10 7 7 10 2 10Z" fill="#7aa564"/></svg>Fully Fenced Backyard</div>
    <div class="chip"><svg width="11" height="11" viewBox="0 0 12 12"><path d="M1 6 L6 2 L11 6 M3 6 V10 H9 V6" stroke="#a07a3c" stroke-width="1.3" fill="none"/></svg>Covered Porch</div>
    <div class="chip"><svg width="11" height="11" viewBox="0 0 12 12"><path d="M6 1 C8 4 10 5 10 8 A4 4 0 0 1 2 8 C2 6 4 5 6 1Z" fill="#e07a2f"/></svg>Outdoor Fire Pit</div>
  </div>
  <div class="photo o1" role="img" aria-label="Photo of the patio fire pit with chairs"></div>
  <div class="photo o2" role="img" aria-label="Photo of the fenced backyard lawn"></div>
  <div class="photo o3" role="img" aria-label="Photo of the covered patio seating"></div>
</section>

<section class="reviews">
  <div class="abs head">
    <div class="eyebrow">Guest Reviews</div>
    <h2 class="h2" style="margin-top:18px">Loved By Guests.<br>Proven By Reviews.</h2>
  </div>
  <div class="abs score">
    <div class="n">4.98 ★</div>
    <div class="c">205 GUEST REVIEWS</div>
    <div class="pills"><span>GUEST FAVORITE</span><span>TOP 1% OF HOMES</span></div>
  </div>
  <div class="abs card" style="left:215px">
    <div class="q">“</div>
    <p>This home is absolutely stunning and in the perfect location. Walking distance to the Tannery Row, great restaurants, and the river. The house was immaculate, well-stocked, and felt like a true home away from home. We'll definitely be back.</p>
    <div class="who">Dana L.<small>August 2024</small></div><div class="stars">★★★★★</div>
  </div>
  <div class="abs card" style="left:477px">
    <div class="q">“</div>
    <p>We brought our two dogs and they had the best time in the fenced backyard. The house itself is beautifully designed — comfortable beds, a well-equipped kitchen, and the fireplace was perfect for cool Bend evenings. Highly recommend.</p>
    <div class="who">Owen &amp; Mia P.<small>July 2024</small></div><div class="stars">★★★★★</div>
  </div>
  <div class="abs card" style="left:738px">
    <div class="q">“</div>
    <p>Cedar Lantern Retreat lived up to every bit of its name. The location is unbeatable and the host communication was exceptional. One of the best Stayvora experiences we've had in years. Already planning our return trip.</p>
    <div class="who">Claire H.<small>September 2024</small></div><div class="stars">★★★★★</div>
  </div>
</section>

<section class="booking">
  <div class="abs copy">
    <div class="eyebrow">Book Your Stay</div>
    <h2>Your Bend Stay Starts<br>Here.</h2>
    <div class="desc">Check your dates, see your total and book your stay directly.</div>
  </div>
  <div class="btn bw">Check Availability</div>
  <div class="btn bo">Book Direct</div>
  <div class="abs fine">SECURE PAYMENT · INSTANT CONFIRMATION · DIRECT BOOKING</div>
  <div class="abs panel">
    <div class="eyebrow">Select Your Dates</div>
    <div class="field" style="left:20px;top:40px;width:156px"><small>CHECK IN</small><span>—</span></div>
    <div class="field" style="left:186px;top:40px;width:154px"><small>CHECK OUT</small><span>—</span></div>
    <div class="field" style="left:20px;top:110px;width:320px"><small>GUESTS</small><span>2 guests</span><small style="position:absolute;right:12px;top:26px">MAX 6</small></div>
    <div class="row" style="top:199px"><span>Nightly rate</span><span>—</span></div>
    <div class="row" style="top:219px"><span>Cleaning fee</span><span>—</span></div>
    <div class="row" style="top:247px;color:var(--white);font-weight:600;border-top:1px solid #4d6858;padding-top:8px"><span>Total</span><span>—</span></div>
    <div class="btn go">Check Availability</div>
  </div>
</section>

<section class="explore">
  <div class="abs" style="left:215px;top:10px">
    <div class="eyebrow">Explore</div>
    <h2 class="h2" style="margin-top:40px">Bend Is Your Backyard</h2>
  </div>
  <div class="abs ex-card" style="left:203px"><div class="fill" role="img" aria-label="Photo of the home in the Tannery Row Quarter" style="background:linear-gradient(180deg,#9bbbd6,#8d9a88 45%,#4e6e35)"></div><div class="veil"></div><h3>Tannery Row Quarter</h3><p>FOOD · SHOPPING · RIVER</p></div>
  <div class="abs ex-card" style="left:413px"><div class="fill" role="img" aria-label="Photo of the outdoor concert pavilion at sunset" style="background:linear-gradient(180deg,#c98fb0,#d99b7a 35%,#5c4a3e 65%,#2b2a22)"></div><div class="veil"></div><h3>Larkspur Fields<br>Pavilion</h3><p>LIVE MUSIC · EVENTS</p></div>
  <div class="abs ex-card" style="left:624px"><div class="fill" role="img" aria-label="Photo of downtown Bend streets and shops" style="background:linear-gradient(180deg,#efece6,#c7bfb2 45%,#6f6253)"></div><div class="veil"></div><h3>Downtown Bend</h3><p>BREWERIES · DINING ·<br>SHOPPING</p></div>
  <div class="abs ex-card" style="left:833px"><div class="fill" role="img" aria-label="Photo of Central Oregon trails and pines" style="background:linear-gradient(180deg,#9ec0d9,#6f8f5a 40%,#3f5f2b)"></div><div class="veil"></div><h3>Central Oregon<br>Outdoors</h3><p>HIKING · TRAILS · ADVENTURE</p></div>
</section>

<section class="cta">
  <div class="eyebrow">Ready to Visit?</div>
  <h2>Make Cedar Lantern Retreat<br>Your Home Base in<br>Bend.</h2>
  <div class="btn go">Check Availability</div>
</section>

<footer class="site-footer">
  <div class="abs brandcol">
    <b>Cedar Lantern Retreat</b>
    <p>Bend, Oregon</p>
    <p>A thoughtfully updated Bend vacation home, steps from the Tannery Row Quarter.</p>
  </div>
  <div class="abs fcol" style="left:479px"><div class="eyebrow">Navigation</div>Home<br>Gallery<br>Reviews<br>FAQ</div>
  <div class="abs fcol" style="left:606px;top:69px">The House<br>Explore Bend<br>Book Direct<br>Contact</div>
  <div class="abs fcol" style="left:741px"><div class="eyebrow">Stay in Touch</div>Questions about the property? We're happy to help.<br><span style="color:var(--white)">Book Direct →</span></div>
  <div class="abs legal"><span>© 2025 Cedar Lantern Retreat · Bend, Oregon. All rights reserved.</span><span>Privacy · Terms</span></div>
</footer>

</body>
</html>
```